Business Card Design for ClearPathVitality

We need the new logo on a business card for 3 employees:
Nora Kettering, PhD, Advanced Instructor and Practitioner of SomaLink Integral Medicine (email: nora@clearpathvitality.com)
Ray Holm, Business Manager (email: ray@clearpathvitality.com)
Bea Marlowe, Administrative Assistant (email: bea@helixsense.com)

Target Market(s)

healthcare professionals

Industry/Entity Type

Alternative Medicine

Contact Information for Business Card

Names, titles, emails (names, titles, emails are in project description), phone, address, website, with logo and tagline. See below for address, phone, website: 418 Alder Ln, Bldg 12, Ste 305
Harbor Vale, CA 95019
707-555-2746
www.clearpathvitality.com
Tagline: Roots of Balance, Light of Renewal

Font styles to use
Other font styles liked:
• Gabriela

Colors
00a990
86cfc6
6b449b
b7a5cd
85abd2
abd036

Requirements
Must have
• Colors and style that match the logo design - shades such as blue, green, purple
• Compatible or same font as in the logo
Nice to have
• Nice if it goes with the theme of Nora's last business card - uploaded below
Should not have
• colors or style in conflict with the logo

```html
<!DOCTYPE html>
<html lang="en">
<head>
<meta charset="UTF-8">
<title>ClearPathVitality – Business Card</title>
<link href="https://fonts.googleapis.com/css2?family=Open+Sans:wght@400;600;700&display=swap" rel="stylesheet">
<style>
  :root {
    --stage: #ebe7e0;
    --card-front: #f1f1f1;
    --ink-blue: #1f3f96;
    --ink-dark: #222428;
    --brand-purple: #4a2a85;
    --back-top: #0a6fc2;
    --back-mid: #2b3f9e;
    --back-bottom: #4a1a78;
    --white: #ffffff;
  }
  * { margin: 0; padding: 0; box-sizing: border-box; }
  html, body { width: 1200px; height: 900px; overflow: hidden; }
  body {
    position: relative;
    background: var(--stage);
    font-family: "Open Sans", Arial, sans-serif;
  }
  .card {
    position: absolute;
    box-shadow: 2px 3px 6px rgba(0,0,0,0.35);
  }
  .card-front {
    left: 320px; top: 88px; width: 580px; height: 357px;
    background: var(--card-front);
    color: var(--ink-dark);
  }
  .brand {
    position: absolute;
    left: 145px; top: 35px; width: 300px; height: 96px;
    display: flex; align-items: center; gap: 12px;
  }
  .brand-dot {
    width: 96px; height: 96px; border-radius: 50%;
    background: var(--brand-purple); flex: none;
  }
  .brand-name {
    font-weight: 600; font-size: 21px; color: var(--brand-purple);
    line-height: 1; white-space: nowrap;
  }
  .person {
    position: absolute; left: 0; top: 153px; width: 580px; text-align: center;
  }
  .person-name {
    font-weight: 700; font-size: 17px; color: var(--ink-blue);
    letter-spacing: 0.2px; line-height: 22px;
  }
  .person-title { font-size: 15px; line-height: 20px; }
  .contact-list {
    position: absolute; right: 290px; top: 219px;
    list-style: none; font-size: 15px; line-height: 21px;
  }
  .contact-list li { display: flex; justify-content: flex-end; align-items: center; gap: 7px; white-space: nowrap; }
  .contact-list svg { width: 13px; height: 13px; flex: none; }
  .address {
    position: absolute; left: 318px; top: 219px;
    font-size: 15px; line-height: 21px; font-style: normal; white-space: nowrap;
  }
  .tagline-row {
    position: absolute; left: 0; top: 308px; width: 580px;
    display: flex; align-items: center; gap: 17px;
  }
  .tagline-rule { height: 1.5px; background: var(--ink-blue); flex: 1; }
  .tagline-rule-end { flex: 0 0 113px; }
  .tagline {
    font-weight: 600; font-size: 15px; color: var(--ink-blue);
    text-transform: uppercase; white-space: nowrap;
  }
  .card-back {
    left: 320px; top: 478px; width: 584px; height: 358px;
    background: linear-gradient(180deg, var(--back-top) 0%, var(--back-mid) 60%, var(--back-bottom) 100%);
    overflow: hidden;
  }
  .back-ring {
    position: absolute; left: 107px; top: -12px; width: 370px; height: 370px;
    border-radius: 50%; border: 14px solid rgba(255,255,255,0.07);
  }
  .back-name {
    position: absolute; left: 0; top: 140px; width: 584px; text-align: center;
    font-weight: 600; font-size: 44px; color: var(--white); line-height: 1;
  }
</style>
</head>
<body>

  <section class="card card-front">
    <div class="brand">
      <span class="brand-dot"></span>
      <span class="brand-name">ClearPathVitality</span>
    </div>

    <div class="person">
      <div class="person-name">RAY HOLM</div>
      <div class="person-title">Business Manager</div>
    </div>

    <ul class="contact-list">
      <li>707-555-2746
        <svg viewBox="0 0 14 14" aria-hidden="true"><path d="M1 5c0-2 2-3 6-3s6 1 6 3l-3 1-1-2H5L4 6z M3 7h8l1 5H2z" fill="var(--ink-blue)"/></svg>
      </li>
      <li>ray@clearpathvitality.com
        <svg viewBox="0 0 14 14" aria-hidden="true"><rect x="1" y="3" width="12" height="8" fill="var(--ink-blue)"/><path d="M1 3l6 5 6-5" stroke="#fff" stroke-width="1" fill="none"/></svg>
      </li>
      <li>www.clearpathvitality.com
        <svg viewBox="0 0 14 14" aria-hidden="true"><circle cx="7" cy="7" r="6" fill="var(--ink-blue)"/><path d="M1 7h12M7 1c-3 3-3 9 0 12M7 1c3 3 3 9 0 12" stroke="#fff" stroke-width="0.8" fill="none"/></svg>
      </li>
    </ul>

    <address class="address">
      418 Alder Ln<br>
      Bldg 12, Ste 305<br>
      Harbor Vale, CA 95019
    </address>

    <div class="tagline-row">
      <span class="tagline-rule"></span>
      <span class="tagline">Roots of Balance, Light of Renewal</span>
      <span class="tagline-rule tagline-rule-end"></span>
    </div>
  </section>

  <section class="card card-back">
    <div class="back-ring"></div>
    <div class="back-name">ClearPathVitality</div>
  </section>

</body>
</html>
```